Insert sheet for our Dog Food Package

We need an information sheet to go inn our pet food package, with branding, and information on ingredients, nutrition and feeding guidance. We will also need two additional items which will be a variation on the label design:
1) Label for package (detailed label about us and our food)
2) Label for outer shipping box (simple label for branding)
We will start with the information, insert page. The winning designer will then deliver the package and box labels as simplified versions of the same graphical theme.
I have attached samples of an earlier drafts of the insert piece. Please disregard the style, form and colors of the examples given. THEY ARE ONLY THERE TO SHOW WHAT INFORMATION SHOULD BE INCLUDED. All colors and style should be from our logo (attached). All graphics, font styles, and placement of elements need to be YOUR creative design - not a copy of the sample we gave. PLEASE READ THIS AND PLEASE DO NOT SUBMIT ANY VARIATION OF THE EXAMPLES!!!!!!!

Target Market(s)

Pet Owners

Industry/Entity Type

Pet Food

Colors
EB3D1F
EC4F4E
F09395
F8D3D4
FCEDEE

Requirements
Must have
• All new design. New colors (based in the palette of our logo), new graphics, new fonts, new placement of elements.
Should not have
• Please disregard the style, form and colors of the examples given. THEY ARE ONLY THERE TO SHOW WHAT INFORMATION SHOULD BE INCLUDED.

```html
<!DOCTYPE html>
<html lang="en">
<head>
<meta charset="UTF-8">
<title>Kanoa – Insert Sheet</title>
<link href="https://fonts.googleapis.com/css2?family=Nunito:wght@400;600;700;800&family=Yellowtail&display=swap" rel="stylesheet">
<style>
  :root{
    --maroon:#2e1019;
    --maroon-line:#4a1a24;
    --red-deep:#b01e24;
    --red-mid:#c4232a;
    --red-bright:#d3282b;
    --orange:#f0522a;
    --white:#ffffff;
    --blush:#fde7e5;
    --rule:#c4232a;
  }
  *{margin:0;padding:0;box-sizing:border-box;}
  html,body{width:1200px;height:2400px;overflow:hidden;background:#e4e4e4;}
  body{position:relative;font-family:"Nunito",sans-serif;}

  .sheet{
    position:absolute;left:40px;top:475px;
    width:986px;height:1276px;
    transform:scale(1.1359);transform-origin:top left;
    background:var(--red-deep);overflow:hidden;color:var(--white);
  }
  .sheet-bg{position:absolute;inset:0;width:986px;height:1276px;}

  .script{font-family:"Yellowtail",cursive;font-weight:400;color:var(--white);position:absolute;}

  .story-title{left:86px;top:100px;font-size:66px;line-height:1;}
  .story-lead{position:absolute;left:88px;top:198px;width:430px;font-size:23px;line-height:29px;font-weight:700;}

  .quote-mark{position:absolute;font-family:Georgia,serif;color:var(--orange);font-weight:700;line-height:1;}
  .quote-open{left:82px;top:325px;font-size:150px;}
  .quote-close{left:460px;top:508px;font-size:90px;}
  .quote-rule{position:absolute;height:2px;background:var(--orange);}
  .quote-rule.top{left:186px;top:404px;width:337px;}
  .quote-rule.bottom{left:112px;top:566px;width:350px;}
  .quote-text{position:absolute;left:112px;top:416px;width:415px;font-size:17.5px;line-height:23.4px;color:var(--blush);}

  .brand{position:absolute;left:600px;top:190px;width:320px;display:flex;align-items:center;justify-content:center;gap:16px;}
  .brand-dot{width:26px;height:26px;border-radius:50%;background:var(--red-bright);}
  .brand-name{font-size:58px;font-weight:800;letter-spacing:6px;color:var(--white);}

  .hero-art{
    position:absolute;left:490px;top:430px;width:460px;height:335px;
    border-radius:48% 52% 40% 60% / 55% 50% 50% 45%;
    background:linear-gradient(120deg,#6b3a26 0%,#7a4530 45%,#f3c7a4 70%,#f5ece4 100%);
    opacity:.9;
  }

  .love-title{left:118px;top:655px;font-size:60px;line-height:64px;}

  .card{
    position:absolute;top:820px;width:350px;height:412px;
    background:var(--maroon);border:3px solid #22090f;border-radius:40px;overflow:hidden;
  }
  .card.nutrition{left:117px;}
  .card.feeding{left:520px;}
  .card-head{height:52px;background:var(--red-deep);display:flex;align-items:center;justify-content:center;font-size:17.5px;font-weight:700;}
  .card-title{text-align:center;font-size:18px;font-weight:700;letter-spacing:.5px;margin-top:22px;}

  .nutri-grid{display:grid;grid-template-columns:1fr auto;column-gap:20px;margin:18px 22px 0;font-size:18px;font-weight:700;line-height:23px;}
  .nutri-grid span:nth-child(even){text-align:right;}
  .card-rule{height:3px;background:var(--rule);margin:0 22px;}
  .nutrition .card-rule.first{margin-top:24px;}
  .ingredients{margin:16px 22px 0;font-size:14.5px;line-height:19.3px;}
  .nutrition .card-rule.last{margin-top:16px;}

  .feed-table{width:calc(100% - 44px);margin:14px 22px 0;border-collapse:collapse;font-size:15px;}
  .feed-table th{font-weight:700;text-align:left;padding:0 0 9px;border-bottom:1px solid var(--rule);font-size:15px;}
  .feed-table td{padding:9px 0 8px;border-bottom:1px solid var(--rule);}
  .feed-table tr:last-child td{border-bottom:none;}
  .feed-table th:last-child,.feed-table td:last-child{text-align:right;}
</style>
</head>
<body>
<main class="sheet">
  <svg class="sheet-bg" viewBox="0 0 986 1276" aria-hidden="true">
    <path d="M0,620 C120,600 230,640 330,690 C420,735 470,760 560,780 C700,810 850,790 986,760 V1276 H0 Z" fill="var(--red-mid)"/>
    <path d="M0,700 C120,660 250,700 360,760 C460,810 560,830 680,830 C800,830 900,810 986,800 V1276 H0 Z" fill="var(--red-bright)"/>
    <path d="M0,0 H986 V405 C900,402 800,380 720,320 C640,260 610,210 520,150 C420,90 300,100 200,85 C110,72 40,55 0,62 Z" fill="var(--maroon)"/>
    <rect x="0" y="1264" width="986" height="12" fill="var(--maroon)"/>
  </svg>

  <h1 class="script story-title">Our Story</h1>
  <p class="story-lead">We Revolutionized the industry. Not Formulated to meet a minimum standard, but to develop the maximum health of the whole dog.</p>

  <span class="quote-mark quote-open">“</span>
  <div class="quote-rule top"></div>
  <p class="quote-text">We didn't just set about to create a food that will pass a minimum standard'. We set out to revolutionize the industry by creating a food that is designed with Superfoods, Wholesome Grains, and Powerful Oils to help your dog achieve their maximum health,happiness and longevity.</p>
  <span class="quote-mark quote-close">”</span>
  <div class="quote-rule bottom"></div>

  <div class="brand">
    <span class="brand-dot"></span>
    <span class="brand-name">KANOA</span>
  </div>

  <div class="hero-art" role="img" aria-label="Illustration of a boy lovingly hugging a brown dog, with small red hearts above"></div>

  <h2 class="script love-title">Prepared with<br>love for Maple</h2>

  <section class="card nutrition">
    <div class="card-head">We prepared the best for Maple</div>
    <h3 class="card-title">NUTRITIONAL INFORMATION</h3>
    <div class="nutri-grid">
      <span>Protein: 15%</span><span>Total Fat: 9.5%</span>
      <span>Crude Fiber: 2.0%</span><span>Moisture: 72%</span>
    </div>
    <div class="card-rule first"></div>
    <p class="ingredients">Potassium Citrate, DiCalcium Phosphate, Calcium Carbonate, Garbanzo Beans, Choline Bitartrate, Taurine, Salt, Zinc Proteinate, Magnesium Oxide, Iron Proteinate, Vitamin B-12, Selenium, Niacin, Riboflavin, Calcium Panthothen- ate, Thiamine, Vitamin A, Vitamin D, Calcium Iodate, Vitamin B6, Folic Acid</p>
    <div class="card-rule last"></div>
  </section>

  <section class="card feeding">
    <div class="card-head">How much should I feed Maple?</div>
    <h3 class="card-title">RECOMMENDED FEEDING PLAN</h3>
    <table class="feed-table">
      <thead><tr><th>APPROXIMATE WEIGHT</th><th>FULL MEAL</th></tr></thead>
      <tbody>
        <tr><td>&lt;20 lbs</td><td>110 g</td></tr>
        <tr><td>20-29 lbs</td><td>200 g</td></tr>
        <tr><td>30-39 lbs</td><td>250 g</td></tr>
        <tr><td>40-54 lbs</td><td>300 g</td></tr>
        <tr><td>55-69 lbs</td><td>350 g</td></tr>
        <tr><td>70-85 lbs</td><td>400 g</td></tr>
        <tr><td>85+ lbs</td><td>500 g</td></tr>
      </tbody>
    </table>
  </section>
</main>
</body>
</html>
```